Travel Company Itinerary and Travel Packet

I run a travel company (agency) that organizes trips (any length i.e. day, week, month, or longer) to countries (Israel, Italy, Greece, etc). Regardless of the destination, we want to provide appealing, professional, and clean materials. We are a firm believer that our product is not just the trip but in everything we do...from our communication to our written/printed materials and online presence. Today we are specifically looking for a template that we can use to share one's trip/itinerary. Ideally what you would create would be a template we could populate with specific information for the client about the day-to-day of their trip, who we are, the hotels they are staying in, the highlights, what to pack, and where to eat, etc. To be more specific, this template should consist of the following:
1. Title Page (including contact info...however this could go where you see fit)
2. About Us (blurb about us at the company),
3. A highlights page of the trip and services included - this could be used as standalone marketing material for our clients to promote trips. (look at the Italy example)
4. A timeline of the process
5. A summary of the trip, bullet point/all one 1 page
6. A day-by-day itinerary page of what they are doing, and where they are staying (each day on its own page - should be the same template repeated for each day.
7. Recommended Hotels to choose from
8. Recommended Restaurants to eat at
9. A pricing page (per person, per group, itemized down to each experience.
10. A packing List
11. A letterhead that could be used for a cover letter
12. Each page should use pictures...a template where one could insert photos per page based on where the trip is going as well as stock imaging that brings the document to life for the reader. (see examples in uploaded files).

We've attached a few that we've seen in the industry that appeals to us and our tastes, but the template we are looking for is even more eye-popping, user-friendly, and communicates a high level of service just by seeing the document. It communicates our brand. Each attached example has elements we like and don't like and will give you. a good picture (we hope), but you'll notice the list we gave you provides a more robust end product...in other words we want more than these examples as we see great potential in including each layer of information with the ability to pick and choose what to include (from all of it to just the highlights page).

Link to Brand Assets- https://files.morvenbay.net/shared/8Kq2Tz7Lw4Xp1Rn6Vb3Yc9Hd5Fj0Ms?view=open
Updates

We need a few days to review the designs and had a few requests for an extension if possible. I've also uploaded sample itineraries for Israel as requested by a few designers. Much appreciated

Target Market(s)

Any client of ours traveling - school, groups, families, big spenders etc

Industry/Entity Type

Travel Industry

Requirements
Must have
• See above list - if clarification is needed, I'm happy to give.

```html
<!DOCTYPE html>
<html lang="en">
<head>
<meta charset="utf-8">
<title>Tavoren – Our Statistics</title>
<link href="https://fonts.googleapis.com/css2?family=Montserrat:wght@300;400;500;600&family=Roboto:ital,wght@0,400;1,400&display=swap" rel="stylesheet">
<style>
  :root {
    --navy: #243a52;
    --orange: #d9852b;
    --yellow: #e3d64b;
    --teal: #2a9cc4;
    --ink: #4a4d52;
    --text: #8c8e92;
    --paper: #f4f4f5;
  }
  html, body {
    margin: 0;
    padding: 0;
    width: 1200px;
    height: 973px;
    overflow: hidden;
    background: var(--paper);
  }
  .spread {
    position: relative;
    width: 1200px;
    height: 973px;
    background: var(--paper);
    font-family: "Montserrat", sans-serif;
    color: var(--text);
  }
  .photo {
    position: absolute;
    top: 0;
    height: 268px;
  }
  .photo--paragliding {
    left: 0;
    width: 600px;
    background: linear-gradient(100deg, #3f7f8a 0%, #6f9aa0 18%, #b59a6e 40%, #9a8a5c 70%, #7f7b55 100%);
  }
  .photo--sandboard {
    left: 600px;
    width: 600px;
    background: linear-gradient(160deg, #b8c8d6 0%, #c98a4e 22%, #c4682e 55%, #a94f22 100%);
  }
  .brand {
    position: absolute;
    left: 32px;
    top: 333px;
    display: flex;
    align-items: center;
    gap: 10px;
  }
  .brand__dot {
    width: 34px;
    height: 34px;
    border-radius: 50%;
    background: var(--orange);
  }
  .brand__name {
    font-family: "Montserrat", sans-serif;
    font-weight: 600;
    font-size: 30px;
    color: var(--navy);
  }
  .divider {
    position: absolute;
    left: 272px;
    top: 318px;
    width: 2px;
    height: 92px;
    background: var(--orange);
  }
  .section-title {
    position: absolute;
    left: 290px;
    top: 322px;
    margin: 0;
    font-weight: 300;
    color: var(--ink);
    line-height: 1.05;
  }
  .section-title__small { display: block; font-size: 30px; font-weight: 400; }
  .section-title__large { display: block; font-size: 45px; }
  .intro {
    position: absolute;
    left: 30px;
    width: 550px;
    margin: 0;
    font-size: 11.2px;
    line-height: 20.3px;
    font-weight: 400;
  }
  .intro--one { top: 432px; }
  .intro--two { top: 644px; }
  .intro--three { top: 813px; }
  .feature-title {
    position: absolute;
    left: 652px;
    top: 298px;
    margin: 0;
    color: var(--ink);
    line-height: 1.1;
  }
  .feature-title__small { display: block; font-size: 22px; font-weight: 500; }
  .feature-title__large { display: block; font-size: 38px; font-weight: 300; }
  .columns {
    position: absolute;
    left: 652px;
    top: 392px;
    width: 510px;
    display: flex;
    gap: 17px;
  }
  .columns p {
    flex: 1;
    margin: 0;
    font-family: "Roboto", sans-serif;
    font-size: 9.3px;
    line-height: 18px;
    text-align: justify;
    hyphens: auto;
  }
  .counter {
    position: absolute;
    top: 724px;
    width: 250px;
  }
  .counter--one { left: 652px; }
  .counter--two { left: 912px; }
  .counter h3 {
    margin: 0 0 14px;
    font-weight: 400;
    font-size: 18px;
    color: var(--ink);
  }
  .counter ul {
    list-style: none;
    margin: 0;
    padding: 0;
  }
  .counter li {
    display: flex;
    align-items: center;
    gap: 10px;
    height: 28px;
    font-family: "Roboto", sans-serif;
    font-style: italic;
    font-size: 9.2px;
  }
  .counter svg { flex: none; }
  .footer-band {
    position: absolute;
    left: 0;
    bottom: 0;
    width: 1200px;
    height: 28px;
  }
  .footer-band svg { position: absolute; inset: 0; }
  .page-number, .web {
    position: absolute;
    bottom: 6px;
    font-size: 12px;
    color: #f5efe4;
  }
  .page-number--left { left: 28px; }
  .page-number--right { right: 28px; }
  .web--left { left: 470px; color: #d9dde3; }
  .web--right { left: 630px; color: #d9dde3; }
</style>
</head>
<body>
<main class="spread">
  <div class="photo photo--paragliding" role="img" aria-label="Photo: tandem paragliders flying over a sandy coastal cliff and sea"></div>
  <div class="photo photo--sandboard" role="img" aria-label="Photo: a man sandboarding down an orange desert dune"></div>

  <div class="brand"><span class="brand__dot"></span><span class="brand__name">Tavoren</span></div>
  <div class="divider"></div>
  <h2 class="section-title"><span class="section-title__small">Our</span><span class="section-title__large">Statistics</span></h2>

  <p class="intro intro--one">Authoritatively megas star fashion there job nee rating Aub need ratin Authoritatively somegas star fashion need not rating Authoritatively megas star fashion there job need rating so thoritatively megas star fashion there jobs need ating Au need megas star fashion Rating Authoritatively megas star fashion there job need rating so thoritatively megas star fashion there job need rating. Authoritatively megas star fashion there job nee rating Aub need ratin Authoritatively somegas star fashion need not rating Authoritatively megas star fashion there job need rating so thoritatively megas star fashion there jobs need ating Au need megas star fashion Rating Authoritatively megas star fashion there job need rating so thoritatively megas star fashion there job need rating.</p>
  <p class="intro intro--two">Authoritatively megas star fashion there job nee rating Aub need ratin Authoritatively somegas star fashion need not rating Authoritatively megas star fashion there job need rating so thoritatively megas star fashion there jobs need ating Au need megas star fashion Rating Authoritatively megas star fashion there job need rating so thoritatively megas star fashion there job need rating. Authoritatively megas star fashion there job nee rating Aub need ratin Authoritatively somegas star fashion need not rating</p>
  <p class="intro intro--three">Authoritatively megas star fashion there job need rating so thoritatively megas star fashion there jobs need ating Au need megas star fashion Rating Authoritatively megas star fashion there job need rating so thoritatively megas star fashion there job need rating.</p>

  <h2 class="feature-title"><span class="feature-title__small">Lorem ipsum</span><span class="feature-title__large">Dolar amet</span></h2>
  <div class="columns">
    <p>Authoritatively so megas star fashion there job nee rating Aub need ratin Authoritatively somegas star fashion need nots go rating uthoritatively megas star fashion there job need rating so thoritatively megas sta fashion there jobs yoo is best need ating Au need megas star fashion Rating Authoritatively so megas star fashion there job nee rating Aub need ratin Authoritatively somegas star fashion need nots go rating uthoritatively megas star fashion there job need Authoritatively so megas star need.</p>
    <p>Authoritatively so megas star fashion there job nee rating Aub need ratin Authoritatively somegas star fashion need nots go rating uthoritatively megas star fashion there job need rating so thoritatively megas sta fashion there jobs yoo is best need ating Au need megas star fashion Rating Authoritatively so megas star fashion there job nee rating Aub need ratin Authoritatively somegas star fashion need nots go rating uthoritatively megas star fashion there job need Authoritatively so megas star need.</p>
    <p>Authoritatively so megas star fashion there job nee rating Aub need ratin Authoritatively somegas star fashion need nots go rating uthoritatively megas star fashion there job need rating so thoritatively megas sta fashion there jobs yoo is best need ating Au need megas star fashion Rating Authoritatively so megas star fashion there job nee rating Aub need ratin Authoritatively somegas star fashion need nots go rating uthoritatively megas star fashion there job need Authoritatively so megas star need.</p>
  </div>

  <section class="counter counter--one">
    <h3>Counter One</h3>
    <ul>
      <li><svg width="14" height="12" viewBox="0 0 14 12"><path d="M1 6.5 5 10.5 13 1.5" fill="none" stroke="var(--teal)" stroke-width="2.6"/></svg>Authoritatively so megas star fashion there job</li>
      <li><svg width="14" height="12" viewBox="0 0 14 12"><path d="M1 6.5 5 10.5 13 1.5" fill="none" stroke="var(--teal)" stroke-width="2.6"/></svg>Nee Rating Aub need ratin Authoritatively somegas</li>
      <li><svg width="14" height="12" viewBox="0 0 14 12"><path d="M1 6.5 5 10.5 13 1.5" fill="none" stroke="var(--teal)" stroke-width="2.6"/></svg>Sta Os fashion need nots go rating uthoritatively</li>
      <li><svg width="14" height="12" viewBox="0 0 14 12"><path d="M1 6.5 5 10.5 13 1.5" fill="none" stroke="var(--teal)" stroke-width="2.6"/></svg>Megas So star fashion there job need rating so</li>
      <li><svg width="14" height="12" viewBox="0 0 14 12"><path d="M1 6.5 5 10.5 13 1.5" fill="none" stroke="var(--teal)" stroke-width="2.6"/></svg>Thoritatively Megas sta fashion there jobs yoo is</li>
      <li><svg width="14" height="12" viewBox="0 0 14 12"><path d="M1 6.5 5 10.5 13 1.5" fill="none" stroke="var(--teal)" stroke-width="2.6"/></svg>Best need ating Au need megas star fashion</li>
    </ul>
  </section>
  <section class="counter counter--two">
    <h3>Counter Two</h3>
    <ul>
      <li><svg width="14" height="12" viewBox="0 0 14 12"><path d="M1 6.5 5 10.5 13 1.5" fill="none" stroke="var(--teal)" stroke-width="2.6"/></svg>Authoritatively so megas star fashion there job</li>
      <li><svg width="14" height="12" viewBox="0 0 14 12"><path d="M1 6.5 5 10.5 13 1.5" fill="none" stroke="var(--teal)" stroke-width="2.6"/></svg>Nee Rating Aub need ratin Authoritatively somegas</li>
      <li><svg width="14" height="12" viewBox="0 0 14 12"><path d="M1 6.5 5 10.5 13 1.5" fill="none" stroke="var(--teal)" stroke-width="2.6"/></svg>Sta Os fashion need nots go rating uthoritatively</li>
      <li><svg width="14" height="12" viewBox="0 0 14 12"><path d="M1 6.5 5 10.5 13 1.5" fill="none" stroke="var(--teal)" stroke-width="2.6"/></svg>Megas So star fashion there job need rating so</li>
      <li><svg width="14" height="12" viewBox="0 0 14 12"><path d="M1 6.5 5 10.5 13 1.5" fill="none" stroke="var(--teal)" stroke-width="2.6"/></svg>Thoritatively Megas sta fashion there jobs yoo is</li>
      <li><svg width="14" height="12" viewBox="0 0 14 12"><path d="M1 6.5 5 10.5 13 1.5" fill="none" stroke="var(--teal)" stroke-width="2.6"/></svg>Best need ating Au need megas star fashion</li>
    </ul>
  </section>

  <footer class="footer-band">
    <svg width="1200" height="28" viewBox="0 0 1200 28" preserveAspectRatio="none">
      <rect x="0" y="0" width="1200" height="28" fill="var(--navy)"/>
      <polygon points="0,0 172,0 200,28 0,28" fill="var(--orange)"/>
      <polygon points="172,0 184,0 212,28 200,28" fill="var(--yellow)"/>
      <polygon points="1028,0 1200,0 1200,28 1000,28" fill="var(--orange)"/>
      <polygon points="1016,0 1028,0 1000,28 988,28" fill="var(--yellow)"/>
    </svg>
    <span class="page-number page-number--left">Page: 01</span>
    <span class="web web--left">www.gotavoren.com</span>
    <span class="web web--right">www.gotavoren.com</span>
    <span class="page-number page-number--right">Page: 01</span>
  </footer>
</main>
</body>
</html>
```